Emergency Vehicle Installer and Security Firm Needs a Business Card

Our company "Corvalta" need a business card for our Emergency Vehicle Equipment Installation and Infrastructure Security Business. We are contract designers, manufacturers and installers for Emergency Vehicle Fleets. This includes installation of Emergency Lights, Sirens, Vehicle Graphics and Radio Communications. We also supply this products to an international market. We also do consultant, and installation of high level security access, alarm and surveillance equipment for medium to large size businesses.

The design should represent a level of trust in our professionalism and expertise. It should visually display our ongoing relationship with the emergency services, but not overtake our commitment to high level security options.

Target Market(s)

Emergency Services and Businesses requiring high level security

Industry/Entity Type

Business

Contact Information for Business Card

*note complete details will be given to the winning designer for revising. The name "Mark Pelling will be used to fill in name".

Mark Pelling
Managing Director
Corvalta NZ Limited
Phone: +64 027 846 20193
Email: mark.pelling@corvalta-example.co.nz

Requirements
Must have
• Card must be in black. Using our logo on the top as supplied. Designers should try having the reverse side as a blurred image of police lights (red and blue) with our logo in greyscale in the centre (this is not particularly a requirement, but feel free to play around with this option).
Nice to have
• A card design that looks good when spot UV printed. A clean compact and graphic design. A grey scale feel on the front (excluding logo, but you can play around with that idea). Rounded smooth text.
Should not have
• Will update this section as designs come through - feel free to submit what you feel would look good.

```html
<!DOCTYPE html>
<html lang="en">
<head>
<meta charset="utf-8">
<title>Corvalta Business Card</title>
<link rel="stylesheet" href="https://fonts.googleapis.com/css2?family=Montserrat:wght@400;500;700&display=swap">
<style>
  :root {
    --page-bg: #2b2b2b;
    --card-black: #050505;
    --logo-grey: #b9b9b9;
    --white: #ffffff;
    --accent-red: #e3202a;
    --divider: #8a8a8a;
    --light-red: #c41a1a;
    --light-blue: #2f4fd8;
    --light-amber: #e8a21c;
  }
  html, body {
    margin: 0;
    width: 1200px;
    height: 900px;
    overflow: hidden;
    background: var(--page-bg);
    font-family: "Montserrat", Arial, sans-serif;
  }
  .canvas {
    position: relative;
    width: 1200px;
    height: 900px;
  }
  .card {
    position: absolute;
    left: 267px;
    width: 665px;
    height: 380px;
    border-radius: 22px;
    overflow: hidden;
    background: var(--card-black);
    box-shadow: 0 10px 30px rgba(0,0,0,0.45);
  }
  .card-back { top: 50px; }
  .card-front { top: 470px; }

  .lights-backdrop {
    position: absolute;
    inset: 0;
    background:
      radial-gradient(ellipse 110px 45px at 22% 52%, rgba(232,162,28,0.85), transparent 70%),
      radial-gradient(ellipse 150px 60px at 16% 56%, rgba(196,26,26,0.8), transparent 75%),
      radial-gradient(ellipse 70px 40px at 40% 40%, rgba(196,26,26,0.75), transparent 70%),
      radial-gradient(ellipse 80px 35px at 48% 22%, rgba(230,230,255,0.8), transparent 70%),
      radial-gradient(ellipse 110px 60px at 48% 25%, rgba(47,79,216,0.7), transparent 75%),
      radial-gradient(ellipse 70px 30px at 70% 8%, rgba(230,230,255,0.8), transparent 70%),
      radial-gradient(ellipse 120px 60px at 72% 10%, rgba(47,79,216,0.7), transparent 75%),
      radial-gradient(ellipse 40px 80px at 88% 40%, rgba(47,79,216,0.6), transparent 75%),
      radial-gradient(ellipse 40px 60px at 78% 72%, rgba(196,26,26,0.6), transparent 75%),
      var(--card-black);
  }
  .back-logo {
    position: absolute;
    left: 0;
    right: 0;
    top: 158px;
    text-align: center;
    font-weight: 700;
    font-size: 68px;
    letter-spacing: 2px;
    color: var(--logo-grey);
  }

  .front-brand {
    position: absolute;
    left: 48px;
    top: 196px;
  }
  .brand-name {
    font-weight: 700;
    font-size: 44px;
    line-height: 1;
    color: var(--white);
    letter-spacing: 1px;
  }
  .brand-legal {
    margin-top: 10px;
    font-weight: 500;
    font-size: 11px;
    letter-spacing: 5.2px;
    color: var(--white);
  }
  .divider {
    position: absolute;
    left: 330px;
    top: 110px;
    width: 1px;
    height: 150px;
    background: var(--divider);
  }
  .contact {
    position: absolute;
    left: 350px;
    top: 116px;
    color: var(--white);
  }
  .contact-name {
    font-weight: 700;
    font-size: 26px;
    color: var(--accent-red);
    line-height: 1.1;
  }
  .contact-role {
    font-size: 15px;
    margin-top: 4px;
  }
  .contact-line {
    display: flex;
    align-items: center;
    gap: 8px;
    font-size: 14px;
    margin-top: 12px;
  }
  .contact-line:first-of-type { margin-top: 22px; }
  .contact-line svg { flex: none; }
</style>
</head>
<body>
<div class="canvas">
  <section class="card card-back">
    <div class="lights-backdrop" role="img" aria-label="Blurred red, blue and amber emergency vehicle lights at night"></div>
    <div class="back-logo">CORVALTA</div>
  </section>

  <section class="card card-front">
    <div class="front-brand">
      <div class="brand-name">CORVALTA</div>
      <div class="brand-legal">CORVALTA NZ LIMITED</div>
    </div>
    <div class="divider"></div>
    <div class="contact">
      <div class="contact-name">MARK PELLING</div>
      <div class="contact-role">Managing Director</div>
      <div class="contact-line">
        <svg width="12" height="12" viewBox="0 0 24 24" aria-hidden="true"><path fill="#e3202a" d="M6.6 10.8a15.1 15.1 0 0 0 6.6 6.6l2.2-2.2c.3-.3.7-.4 1-.2 1.1.4 2.3.6 3.6.6.6 0 1 .4 1 1V20c0 .6-.4 1-1 1A17 17 0 0 1 3 4c0-.6.4-1 1-1h3.5c.6 0 1 .4 1 1 0 1.3.2 2.5.6 3.6.1.3 0 .7-.2 1z"/></svg>
        <span>+64 027 846 20193</span>
      </div>
      <div class="contact-line">
        <svg width="12" height="10" viewBox="0 0 24 18" aria-hidden="true"><rect x="1" y="1" width="22" height="16" rx="2" fill="none" stroke="#e3202a" stroke-width="2.2"/><path d="M2 2l10 8 10-8" fill="none" stroke="#e3202a" stroke-width="2.2"/></svg>
        <span>mark.pelling@corvalta-example.co.nz</span>
      </div>
    </div>
  </section>
</div>
</body>
</html>
```